Communication and Marketing agency needs a new presentation card

We are a group of communication and marketing agencies specialized in companies that are in the logistics and industrial sector. The head agency is TELVANO Grupo and the group consists of 4 agencies: TELVANO Media, TELVANO Digital, TELVANO Research and EnlazaPorImagen. We hace 4 offices in Spain (Madrid, Barcelona, Valencia and Murcia). We are looking for a clean and attractive design that transmits our experience, brand presence in the market and knowledge to those who receive the card.It has to maintain the colors of the logo that is attached.
Target Market(s)
logistics and industrial sector
Marketing department
Clean and attractive design

```html
<!DOCTYPE html>
<html lang="es">
<head>
<meta charset="utf-8">
<title>TELVANO Grupo – Tarjeta de presentación</title>
<link href="https://fonts.googleapis.com/css2?family=Cinzel:wght@400;500&display=swap" rel="stylesheet">
<style>
  :root {
    --stage: #e3e2e8;
    --card-base: #141414;
    --card-glow: #2e2e30;
    --tile: #232323;
    --tile-alt: #1d1d1d;
    --icon: #070707;
    --contact-text: #6e6e6e;
    --brand-red: #c8141e;
  }
  * { margin: 0; padding: 0; box-sizing: border-box; }
  html, body {
    width: 1200px; height: 900px; overflow: hidden;
    background: var(--stage);
  }
  .stage {
    width: 1200px; height: 900px;
    display: flex; flex-direction: column;
    align-items: center; justify-content: center; gap: 50px;
  }
  .card {
    width: 630px; height: 360px;
    position: relative; overflow: hidden;
    background: var(--card-base);
    box-shadow: 0 10px 30px rgba(0,0,0,0.18);
  }
  .card--front {
    background: radial-gradient(ellipse 55% 60% at 45% 38%, var(--card-glow) 0%, var(--card-base) 75%);
  }
  .brand-name {
    font-family: "Cinzel", serif;
    font-weight: 500;
    color: var(--brand-red);
    letter-spacing: 0.12em;
    white-space: nowrap;
  }
  .card--front .brand-name {
    position: absolute; left: 50%; top: 50%;
    transform: translate(-50%, -50%);
    font-size: 46px;
  }
  .contact-row {
    position: absolute; left: 22px; right: 22px; top: 22px;
    height: 195px;
    display: grid; grid-template-columns: repeat(4, 1fr); gap: 4px;
  }
  .contact-tile {
    background: var(--tile);
    display: flex; flex-direction: column; align-items: center;
    padding-top: 34px; gap: 18px;
  }
  .contact-tile:nth-child(even) { background: var(--tile-alt); }
  .contact-icon { width: 46px; height: 46px; }
  .contact-text {
    font-family: "Cinzel", serif;
    font-size: 10px; line-height: 1.5;
    color: var(--contact-text);
    text-align: center; letter-spacing: 0.04em;
    padding: 0 6px;
    white-space: nowrap;
  }
  .card--back .brand-name {
    position: absolute; left: 50%; top: 282px;
    transform: translate(-50%, -50%);
    font-size: 30px;
  }
  .card--back::after {
    content: ""; position: absolute; left: 0; right: 0; bottom: 0; height: 150px;
    background: radial-gradient(ellipse 40% 60% at 50% 50%, rgba(255,255,255,0.05), transparent 70%);
    pointer-events: none;
  }
</style>
</head>
<body>
<main class="stage">
  <section class="card card--back" aria-label="Reverso de la tarjeta">
    <div class="contact-row">
      <div class="contact-tile">
        <svg class="contact-icon" viewBox="0 0 46 46" aria-hidden="true">
          <g fill="none" stroke="var(--icon)" stroke-width="3">
            <circle cx="23" cy="23" r="19"/>
            <ellipse cx="23" cy="23" rx="8" ry="19"/>
            <line x1="4" y1="23" x2="42" y2="23"/>
            <line x1="8" y1="13" x2="38" y2="13"/>
            <line x1="8" y1="33" x2="38" y2="33"/>
            <line x1="23" y1="4" x2="23" y2="42"/>
          </g>
        </svg>
        <p class="contact-text">715 309-2284 (4471)</p>
      </div>
      <div class="contact-tile">
        <svg class="contact-icon" viewBox="0 0 46 46" aria-hidden="true">
          <rect x="2" y="9" width="42" height="28" fill="var(--icon)"/>
          <polyline points="2,9 23,26 44,9" fill="none" stroke="var(--tile-alt)" stroke-width="2"/>
        </svg>
        <p class="contact-text">info@<br>telvanogrupo.<br>com</p>
      </div>
      <div class="contact-tile">
        <svg class="contact-icon" viewBox="0 0 46 46" aria-hidden="true">
          <rect x="13" y="3" width="20" height="40" rx="3" fill="none" stroke="var(--icon)" stroke-width="3"/>
          <line x1="20" y1="38" x2="26" y2="38" stroke="var(--icon)" stroke-width="2.5"/>
        </svg>
        <p class="contact-text">www.<br>telvanogrupo.<br>com</p>
      </div>
      <div class="contact-tile">
        <svg class="contact-icon" viewBox="0 0 46 46" aria-hidden="true">
          <path d="M23 43 C13 30 8 23 8 17 A15 15 0 0 1 38 17 C38 23 33 30 23 43 Z" fill="var(--icon)"/>
          <circle cx="23" cy="17" r="5" fill="var(--tile-alt)"/>
        </svg>
        <p class="contact-text">48 Paseo Lirio Alto<br>Madrid, Spain 28014</p>
      </div>
    </div>
    <p class="brand-name">TELVANO Grupo</p>
  </section>

  <section class="card card--front" aria-label="Anverso de la tarjeta">
    <p class="brand-name">TELVANO Grupo</p>
  </section>
</main>
</body>
</html>
```